Brivan Learning Web Design Project

Who We are:
Brivan Learning is education information portal/ magazine, providing information about the Chinese and International education markets. Our aim is to help school principals improve there curriculum, and parents in understanding this curriculum.

Project Brief:
The site will include education news updates, educational services, curriculum developments and overseas study. We hope the site represents the cross cultural bridge between the west and east. The site will cover both the Sciences and Arts.

Note:
The logo design competition is also underway so we only need the website design

What We want:
This competition is for Design only no coding!
Design a home page based on Template 1,2 or 3. I only need to select one.
The design of an article page.

Optional
Design a Microsoft Windows metro style splash page.

Sites We like:
http://www.qz.com.cn/wordsparrow/default.aspx
http://www.velmaracademicpost.co.uk/
http://pvro.orbalinkstudy.net/

Template Explanations:
Template 1-
The main information has a dynamic sliding category view that when clicked displays the relevant info.
In addition to the main upper menu it also has a left hand sliding menu that pops out on click or gesture

Template 2-
Has limited number of Articles most of the menus are drop downs from the top menu

Template 3-
No Top menu

Target Market(s)

Teachers, principals and parents

Industry/Entity Type

Education

Requirements
Should not have
• kindergarten preschool feel

```html
<!DOCTYPE html>
<html lang="en">
<head>
<meta charset="utf-8">
<title>Brivan Learning</title>
<link href="https://fonts.googleapis.com/css2?family=Crimson+Text:wght@600;700&family=Exo:wght@300;700&family=Oswald:wght@500&family=Ubuntu:wght@400;500&display=swap" rel="stylesheet">
<style>
:root{
  --page:#ebe8e3;
  --white:#ffffff;
  --red:#d8302b;
  --red-dark:#b81f1b;
  --blue-nav:#2b62a8;
  --text:#3a3a3a;
  --muted:#888;
  --link:#a05a12;
  --panel:#f1f1f1;
  --green:#3aa63a;
  --sky:#2a8fd4;
  --footer:#333333;
  --footer-text:#d8d8d8;
  --footer-link:#a9a9a9;
}
*{margin:0;padding:0;box-sizing:border-box}
html,body{width:926px;height:1200px;overflow:hidden}
body{background:var(--page);font-family:"Ubuntu",sans-serif;color:var(--text);position:relative}
.abs{position:absolute}

.site-header{left:78px;top:22px;width:770px;height:80px;background:var(--white)}
.brand{left:16px;top:26px;display:flex;align-items:center;gap:8px}
.brand-mark{width:26px;height:26px;border-radius:50%;background:var(--blue-nav)}
.brand-name{font-family:"Ubuntu",sans-serif;font-weight:500;font-size:17px;color:var(--red)}
.search{left:475px;top:27px;width:245px;height:26px;border:1px solid #ddd;background:#fff;font-size:9px;font-style:italic;color:#aaa;padding:7px 9px}
.search-btn{left:725px;top:27px;width:29px;height:26px;background:var(--red);border-radius:2px}

.main-nav{left:78px;top:102px;width:770px;height:34px;background:var(--red);display:flex;border-bottom:2px solid var(--red-dark)}
.main-nav a{flex:1;font-family:"Crimson Text",serif;font-weight:700;font-size:13px;color:#fff;text-decoration:none;display:flex;align-items:center;justify-content:center;height:32px;white-space:nowrap}
.main-nav a.active{background:var(--blue-nav);flex:0 0 83px}

.content{left:78px;top:146px;width:770px;height:812px;background:var(--white)}

.tile{left:86px;width:46px;height:54px;display:flex;align-items:center;justify-content:center}
.social{left:96px;width:20px;height:20px;border-radius:50%}

.slider{left:140px;top:153px;width:569px;height:232px;background:linear-gradient(90deg,#d9d6d3 0%,#6a6560 45%,#3e3f43 100%)}
.slider h2{position:absolute;left:276px;top:50px;font-family:"Exo",sans-serif;font-weight:700;font-size:27px;line-height:34px;color:#fff;text-shadow:0 2px 3px rgba(0,0,0,.5);white-space:nowrap}
.slider .btn{position:absolute;left:276px;top:124px;background:#fff;border-radius:3px;padding:6px 7px;font-family:"Exo",sans-serif;font-weight:700;font-size:13px;color:#222}

.section-title{left:140px;top:398px;width:569px;height:22px;display:flex;align-items:center;gap:9px}
.section-title .bar{height:16px;background:linear-gradient(#5fc45a,#279a2a);border-radius:8px}
.section-title .bar.short{flex:0 0 24px}
.section-title .bar.long{flex:1}
.section-title h3{font-family:"Exo",sans-serif;font-weight:300;font-size:19px;line-height:22px;color:var(--sky);white-space:nowrap}

.articles{left:140px;top:426px;width:569px;height:338px;background:var(--panel)}
.card{position:absolute;width:272px}
.card .photo{height:97px}
.card p{font-size:10.5px;line-height:14px;margin:10px 2px 0;color:#333}
.card a{display:block;font-size:10px;color:var(--link);text-decoration:none;margin:6px 2px 0}

.cat-bar{left:140px;width:569px;height:43px;font-family:"Crimson Text",serif;font-weight:700;font-size:20px;color:#fff}
.cat-bar span{position:absolute;top:50%;transform:translate(-50%,-50%);white-space:nowrap}
.cat-bar .c1{left:220px}
.cat-bar .c2{left:365px}

.ad{left:718px;width:123px;background:linear-gradient(#c52a24 0%,#8e1a17 30%,#c8c8c8 60%,#7d1613 100%);color:#fff;text-align:center;overflow:hidden}
.ad .ad-name{font-family:"Ubuntu",sans-serif;font-weight:500;font-size:13px;margin-top:11px}
.ad .ad-head{font-family:"Oswald",sans-serif;font-size:14px;line-height:14px;margin-top:8px}
.ad .box{margin:18px auto 0;width:86px;height:118px;background:linear-gradient(135deg,#2a2a2a,#6a1410 60%,#e0a030)}
.ad ul{list-style:none;text-align:left;margin:58px 0 0 20px;font-family:"Oswald",sans-serif;font-size:11px;line-height:17px}
.ad li::before{content:"✓ ";color:#f0d0c0}
.ad .dl{margin:10px auto 0;width:84px;height:46px;background:#1e1e1e;border:2px solid #f0f0f0;border-radius:6px;font-family:"Oswald",sans-serif;font-size:14px;line-height:15px;padding-top:6px}

.site-footer{left:0;top:966px;width:926px;height:234px;background:var(--footer)}
.f-col{position:absolute;top:28px}
.f-col h4{font-weight:400;font-size:12px;color:var(--footer-text);white-space:nowrap}
.f-col ul{list-style:none;margin-top:17px}
.f-col li{font-size:8.5px;line-height:16px;color:var(--footer-link);text-decoration:underline;white-space:nowrap}
.f-social{display:flex;gap:12px;margin-top:16px}
.f-social span{width:24px;height:24px;background:#3b6fb4;border-radius:2px}
.newsletter{display:flex;margin-top:15px;width:204px;height:26px;background:#2a2a2a}
.newsletter .in{flex:1;font-size:8px;font-style:italic;color:#777;padding:9px 9px;white-space:nowrap}
.newsletter .sub{background:var(--red);color:#fff;font-size:10px;padding:6px 10px;margin:2px}
.f-rule{left:92px;top:189px;width:742px;height:1px;background:#555}
.copyright{left:92px;top:205px;font-size:9px;color:#aaa}
</style>
</head>
<body>

<header class="site-header abs">
  <div class="brand abs"><span class="brand-mark"></span><span class="brand-name">BRIVAN LEARNING</span></div>
  <div class="search abs">Please enter your search</div>
  <div class="search-btn abs">
    <svg width="29" height="26" viewBox="0 0 29 26"><circle cx="13.5" cy="12" r="4.5" fill="none" stroke="#fff" stroke-width="2"/><line x1="16.5" y1="15" x2="19.5" y2="18" stroke="#fff" stroke-width="2.2"/></svg>
  </div>
</header>

<nav class="main-nav abs">
  <a class="active" href="#">Home</a>
  <a href="#">About Us</a>
  <a href="#">Service</a>
  <a href="#">New &amp; Event</a>
  <a href="#">Blog</a>
  <a href="#">Brivan Learning</a>
  <a href="#">Contact Us</a>
</nav>

<div class="content abs"></div>

<div class="tile abs" style="top:153px;background:#c9437c"><svg width="28" height="26" viewBox="0 0 28 26" fill="none" stroke="#fff" stroke-width="2"><path d="M3 12 L14 3 L25 12"/><path d="M6 10 V23 H22 V10"/><ellipse cx="16" cy="17" rx="5" ry="3"/></svg></div>
<div class="tile abs" style="top:209px;background:#dea823"><svg width="28" height="24" viewBox="0 0 28 24" fill="#fff"><ellipse cx="11" cy="11" rx="9" ry="6"/><path d="M6 15 L4 21 L11 16Z"/><ellipse cx="19" cy="8" rx="7" ry="5" fill="none" stroke="#fff" stroke-width="2"/></svg></div>
<div class="tile abs" style="top:265px;background:#3aa63a"><svg width="26" height="26" viewBox="0 0 26 26" stroke="#fff" stroke-width="3" stroke-linecap="round"><line x1="5" y1="5" x2="21" y2="21"/><line x1="21" y1="5" x2="5" y2="21"/></svg></div>
<div class="tile abs" style="top:321px;background:#2a8fd4"><svg width="22" height="26" viewBox="0 0 22 26" fill="none" stroke="#fff" stroke-width="2"><path d="M3 2 H14 L19 7 V24 H3Z"/><line x1="7" y1="11" x2="15" y2="11"/><line x1="7" y1="15" x2="15" y2="15"/><line x1="7" y1="19" x2="15" y2="19"/></svg></div>
<div class="tile abs" style="top:377px;background:#8a4aa6"><svg width="28" height="24" viewBox="0 0 28 24" fill="none" stroke="#fff" stroke-width="2"><rect x="2" y="2" width="24" height="20"/><line x1="2" y1="7" x2="26" y2="7"/><rect x="6" y="11" width="7" height="7" fill="#fff"/><line x1="16" y1="12" x2="22" y2="12"/><line x1="16" y1="16" x2="22" y2="16"/></svg></div>
<div class="tile abs" style="top:433px;background:#6e1f7a"><svg width="26" height="26" viewBox="0 0 26 26" fill="none" stroke="#fff" stroke-width="2"><rect x="3" y="3" width="20" height="13"/><line x1="13" y1="16" x2="7" y2="24"/><line x1="13" y1="16" x2="19" y2="24"/><line x1="7" y1="8" x2="15" y2="8"/><line x1="7" y1="12" x2="12" y2="12"/></svg></div>
<div class="tile abs" style="top:489px;background:#b06a22"><svg width="24" height="24" viewBox="0 0 24 24" fill="#fff"><path d="M5 17 C3 15 4 13 6 13 L9 15 C14 12 15 10 16 8 L14 5 C14 3 16 2 18 4 C21 7 20 10 17 14 C13 19 9 21 5 17Z"/></svg></div>

<div class="social abs" style="top:666px;background:#d9406f"></div>
<div class="social abs" style="top:710px;background:#dea823"></div>
<div class="social abs" style="top:754px;background:#3aa63a"></div>
<div class="social abs" style="top:798px;background:#2a8fd4"></div>
<div class="social abs" style="top:842px;background:#8a4aa6"></div>
<div class="social abs" style="top:886px;background:#e04fb3"></div>
<div class="social abs" style="top:930px;background:#b06a22"></div>

<section class="slider abs" role="img" aria-label="Photo of a smiling student holding a red folder in a library">
  <h2>Contrairement à unei<br>nion répandue</h2>
  <span class="btn">Read More</span>
</section>

<div class="section-title abs">
  <span class="bar short"></span>
  <h3>Latest Articles</h3>
  <span class="bar long"></span>
</div>

<section class="articles abs">
  <article class="card" style="left:8px;top:8px">
    <div class="photo" role="img" aria-label="Photo of a group of smiling students" style="background:linear-gradient(90deg,#3a2e2a,#b89a88,#5a4a44)"></div>
    <p>Plusieurs variations de Lorem Ipsumpeuve nt être trouvées ici ou.</p>
    <a href="#">Read More »</a>
  </article>
  <article class="card" style="left:290px;top:8px">
    <div class="photo" role="img" aria-label="Photo of a student studying at a desk by a window" style="background:linear-gradient(90deg,#6a5040,#c8b8a4,#dfe6e4)"></div>
    <p>De nombreuses suites logicielles de mise en page ou éditeurs de sites Web.</p>
    <a href="#">Read More »</a>
  </article>
  <article class="card" style="left:8px;top:177px">
    <div class="photo" role="img" aria-label="Photo of a student writing in a notebook" style="background:linear-gradient(90deg,#4a4848,#9a9894,#5c5a58)"></div>
    <p>Letraset contenant des passages duLorem Ipsum, et, plus récemment.</p>
    <a href="#">Read More »</a>
  </article>
  <article class="card" style="left:290px;top:177px">
    <div class="photo" role="img" aria-label="Photo of a smiling graduate in a cap" style="background:linear-gradient(90deg,#1e1c1c,#b08670,#3c3a38)"></div>
    <p>Suprêmes Maux) de Cicéron. Cet ouvrage, très popul aire pendant la.</p>
    <a href="#">Read More »</a>
  </article>
</section>

<div class="cat-bar abs" style="top:773px;background:linear-gradient(#9bd64a,#5aa822)"><span class="c1">Europe</span><span class="c2">Drama</span></div>
<div class="cat-bar abs" style="top:818px;background:linear-gradient(#ffa41e,#f07c00)"><span class="c1">Asia</span><span class="c2">Science</span></div>
<div class="cat-bar abs" style="top:863px;background:linear-gradient(#d42a24,#b0150f)"><span class="c1">Usa</span><span class="c2">English</span></div>
<div class="cat-bar abs" style="top:909px;background:linear-gradient(#36b0ee,#1a8ad4)"><span class="c1">France</span><span class="c2">Franch</span></div>

<aside class="ad abs" style="top:153px;height:462px">
  <div class="ad-name">SiteForge Studio</div>
  <div class="ad-head">Create<br>your website<br>in just<br>5 steps</div>
  <div class="box" role="img" aria-label="Software product box"></div>
  <ul><li>1400 Templates</li><li>Webshop</li><li>RSS feed</li><li>Member Areas</li><li>Blog</li></ul>
  <div class="dl">DOWNLOAD<br>IT NOW!</div>
</aside>
<aside class="ad abs" style="top:623px;height:327px">
  <div class="ad-name">SiteForge Studio</div>
  <div class="ad-head">Create<br>your website<br>in just<br>5 steps</div>
  <div class="box" role="img" aria-label="Software product box"></div>
  <ul style="margin-top:58px"><li>1400 Templates</li></ul>
</aside>

<footer class="site-footer abs">
  <div class="f-col" style="left:92px"><h4>Company</h4><ul><li>Contrairement</li><li>Opinion répandue</li><li>Pas simplement du</li><li>Texte aléatoire</li></ul></div>
  <div class="f-col" style="left:226px"><h4>Dictionnaire de</h4><ul><li>Plusieurs variations</li><li>De Lorem Ipsum</li><li>Vent être</li></ul></div>
  <div class="f-col" style="left:367px"><h4>Trouvées ici ou</h4><ul><li>Siècle est reproduit</li><li>Dessous pour les</li><li>CurieuxPlusieurs varia-</li><li>tions</li><li>De Lorem Ipsum</li></ul></div>
  <div class="f-col" style="left:505px"><h4>Embarassantes</h4><ul><li>L'extrait standard</li><li>Utilisé depuis</li><li>Siècle est reproduit</li><li>Dessous pour les</li><li>Curieux</li><li>Vous voulez utiliser</li><li>Passage du Lorem</li></ul></div>
  <div class="f-col" style="left:631px">
    <h4>Stay updates on our Socail Network</h4>
    <div class="f-social"><span></span><span style="background:#3fa9e0"></span><span style="background:#1f6fa8"></span></div>
    <h4 style="margin-top:14px">Join Our Newsletter</h4>
    <div class="newsletter"><span class="in">Enter your email address</span><span class="sub">Subscribe</span></div>
  </div>
  <div class="f-rule abs"></div>
  <div class="copyright abs">© Copyrights 2013 All rights Reserved</div>
</footer>

</body>
</html>
```